Design an amazing Wallpaper for a wall heating in a company

hello designer,
we would like to install a wall heating which can be printed with a wallpaper. for this we are looking for a mega cool picture in which our product logo is integrated.
we create for companies an occupational health and safety management software which helps companies to protect their employees.
The name Velundra is derived from the following ->
A Praetorium or Pretorium was originally in the Roman Republic the tent of the commander in a legion camp (castra) - the safest place in the camp.
Praetorians were a guard force deployed by the Roman emperors.
the association & keywords: administration, security, strategy
We call the employees responsible for occupational safety in the company Praetorians. These Praetorians do not protect the Emperor, but the employees.
We therefore imagine a wallpaper in Roman style, which has a connection with our product, the name, and the key words management, security, strategy.
The logo must be integrated into the image. If the coloring can still be included, that would be great.
As an example the following picture could show the red colors in green and then the name (without the helmet from the logo) together with a slogan like "VELUNDRA - we safe your life".
https://www.bildmosaik-archiv.at/unifformen-legionary-brutal-r%C3%B6misches-71349208.html
Please submit your own proposals. The pictures may be either in the fantasy / gaming direction or in a very modern line / comic drawing.
you can test your design here -> click on the orange button "free individualize"
https://www.lindqvarm-technik.de/bild-serie/
we are looking forward to your suggestions!

```html
<!DOCTYPE html>
<html lang="en">
<head>
<meta charset="utf-8">
<title>Velundra – Wall Heating Wallpaper</title>
<link rel="stylesheet" href="https://fonts.googleapis.com/css2?family=Cinzel:wght@500&display=swap">
<style>
  :root {
    --paper: #ffffff;
    --key-grey: #a9a9a9;
    --key-grey-light: #c9c9c9;
    --key-green: #6cbf3f;
    --key-green-dark: #3f5a31;
    --key-lime: #8cc63f;
    --guard-grey: #d4d4d4;
    --guard-grey-soft: #ededed;
    --brand-ink: #36452c;
    --brand-mark: #7cc242;
  }
  html, body {
    margin: 0;
    padding: 0;
    width: 1200px;
    height: 1200px;
    overflow: hidden;
    background: var(--paper);
  }
  .wallpaper {
    position: relative;
    width: 1200px;
    height: 1200px;
    background: var(--paper);
  }
  .frames {
    position: absolute;
    inset: 0;
  }
  .frame { fill: none; }
  .frame--grey { stroke: url(#fade-grey); }
  .frame--grey-light { stroke: url(#fade-grey-light); }
  .frame--green { stroke: var(--key-green); opacity: .8; }
  .frame--green-dark { stroke: var(--key-green-dark); opacity: .85; }
  .frame--lime { stroke: var(--key-lime); opacity: .8; }
  .guard-line {
    position: absolute;
    left: 344px;
    top: 518px;
    width: 512px;
    height: 124px;
    background: linear-gradient(90deg, var(--guard-grey) 0%, var(--guard-grey-soft) 50%, var(--guard-grey) 100%);
    -webkit-mask-image: linear-gradient(180deg, #000 0%, #000 60%, transparent 100%);
    mask-image: linear-gradient(180deg, #000 0%, #000 60%, transparent 100%);
  }
  .brand-mark {
    position: absolute;
    left: 566px;
    top: 532px;
    width: 64px;
    height: 64px;
    border-radius: 50%;
    background: var(--brand-mark);
  }
  .brand-name {
    position: absolute;
    left: 0;
    top: 644px;
    width: 1200px;
    margin: 0;
    padding-left: 0.24em;
    box-sizing: border-box;
    text-align: center;
    font-family: "Cinzel", "Times New Roman", serif;
    font-weight: 500;
    font-size: 50px;
    letter-spacing: 0.24em;
    color: var(--brand-ink);
    line-height: 1;
  }
</style>
</head>
<body>
  <main class="wallpaper">
    <svg class="frames" width="1200" height="1200" viewBox="0 0 1200 1200" role="img" aria-label="Nested Greek key meander borders in grey and green">
      <defs>
        <linearGradient id="fade-grey" x1="0" y1="0" x2="1" y2="1">
          <stop offset="0" stop-color="#a9a9a9"/>
          <stop offset="0.5" stop-color="#ececec"/>
          <stop offset="1" stop-color="#a9a9a9"/>
        </linearGradient>
        <linearGradient id="fade-grey-light" x1="0" y1="0" x2="1" y2="1">
          <stop offset="0" stop-color="#c4c4c4"/>
          <stop offset="0.5" stop-color="#f0f0f0"/>
          <stop offset="1" stop-color="#c4c4c4"/>
        </linearGradient>
      </defs>
      <rect class="frame frame--grey" x="136" y="318" width="928" height="560" stroke-width="26"/>
      <rect class="frame frame--green" x="176" y="358" width="848" height="480" stroke-width="24"/>
      <rect class="frame frame--grey-light" x="211" y="391" width="778" height="414" stroke-width="20"/>
      <rect class="frame frame--green-dark" x="242" y="416" width="716" height="362" stroke-width="18"/>
      <rect class="frame frame--grey-light" x="272" y="440" width="656" height="316" stroke-width="14"/>
      <rect class="frame frame--lime" x="302" y="462" width="596" height="272" stroke-width="14"/>
      <rect class="frame frame--grey-light" x="330" y="484" width="540" height="226" stroke-width="10"/>
    </svg>
    <div class="guard-line" role="img" aria-label="Row of Roman guards with spears and round shields in soft grey"></div>
    <div class="brand-mark"></div>
    <h1 class="brand-name">VELUNDRA</h1>
  </main>
</body>
</html>
```